Income Tax and Accounting Brochure

I need a brochure using my new logo (file attached). I do tax work and accounting work. I am an EA (QDX Enrolled Agent - logo attached) and would like this incorporated into the brochure. I also have a MSA in Accounting. Please incorporate the text that I have provided in the brochure.

Target Market(s)

Tax Clients - both business and individuals

Industry/Entity Type

Accounting

Colors
0054AA
0677BA
7BADD7
CADEEF
E8F1F8

Requirements
Must have
• Use my logo and the QDX EA file in the brochure
Nice to have
• I would like to see a brochure that I can customize with my own text if possible.

```html
<!DOCTYPE html>
<html lang="en">
<head>
<meta charset="utf-8">
<title>Halvern Accounting &amp; Consulting — Tax &amp; Accounting Services</title>
<link rel="stylesheet" href="https://fonts.googleapis.com/css2?family=Josefin+Sans:wght@300;400&family=Source+Sans+3:wght@400;500&display=swap">
<style>
  :root {
    --brand-blue: #1c3fe0;
    --cover-blue: #0b40f0;
    --accent-red: #cc1020;
    --ink: #222629;
    --night: #0d1117;
    --paper: #ffffff;
    --band: #cfecf6;
    --band-line: #e9f6fb;
  }
  * { margin: 0; padding: 0; box-sizing: border-box; }
  html, body { width: 1200px; height: 848px; overflow: hidden; background: var(--paper); }
  .brochure { position: relative; width: 1200px; height: 848px; display: flex; }
  .panel { position: relative; width: 400px; height: 848px; overflow: hidden; }

  /* Inside panel */
  .panel--inside { background: var(--paper); }
  .feature { position: absolute; left: 0; width: 400px; padding: 0 60px; text-align: center; }
  .feature--top { top: 48px; }
  .feature--bottom { top: 534px; }
  .feature__title {
    font-family: "Source Sans 3", sans-serif; font-weight: 400;
    font-size: 23px; line-height: 29px; color: var(--brand-blue);
    margin: 0 -20px;
  }
  .feature__lead {
    font-family: "Source Sans 3", sans-serif; font-weight: 400;
    font-size: 13.5px; line-height: 17px; color: var(--accent-red);
    margin-top: 14px;
  }
  .copy {
    font-family: "Josefin Sans", sans-serif; font-weight: 300;
    font-size: 12.6px; line-height: 17px; color: var(--ink);
  }
  .feature .copy { margin-top: 11px; }
  .feature .copy + .copy { margin-top: 17px; }

  .band {
    position: absolute; left: 0; top: 355px; width: 400px; height: 139px;
    background: var(--band);
  }
  .band__line { position: absolute; left: 0; width: 400px; height: 1px; background: var(--band-line); }
  .feature-photo {
    position: absolute; left: 107px; top: 329px; width: 188px; height: 188px; border-radius: 50%;
    background: radial-gradient(circle at 40% 35%, #8fb4f4 0%, #3c72e6 45%, #1d4fd8 75%, #a9c4f2 100%);
  }

  /* Back panel */
  .panel--back { background: var(--night); }
  .about {
    position: absolute; top: 113px; left: 70px; width: 260px; text-align: center; color: #e8eaee;
  }
  .about .copy { color: #e8eaee; }
  .about .copy + .copy { margin-top: 17px; }
  .brand {
    position: absolute; top: 533px; left: 462px; left: 62px;
    display: flex; align-items: center; gap: 12px;
  }
  .brand__mark { width: 66px; height: 66px; border-radius: 50%; background: var(--brand-blue); flex: none; }
  .brand__name {
    font-family: "Source Sans 3", sans-serif; font-weight: 500;
    color: var(--brand-blue); font-size: 19px; line-height: 25px; letter-spacing: 0.5px;
  }
  .brand__name span { display: block; letter-spacing: 3.6px; }
  .credential-badge {
    position: absolute; left: 83px; top: 688px; width: 243px; height: 63px;
    background: var(--paper);
  }

  /* Cover panel */
  .panel--cover { background: var(--cover-blue); }
  .cover-photo {
    position: absolute; left: 0; top: 0; width: 400px; height: 631px;
    background:
      radial-gradient(circle at 68% 44%, rgba(255,80,60,0.55) 0%, rgba(255,80,60,0) 18%),
      linear-gradient(160deg, #f2f5fb 0%, #c9d6ee 30%, #6d8fd6 55%, #1f4fc4 80%, #a8bde6 100%);
  }
  .cover-rule { position: absolute; left: 0; top: 631px; width: 400px; height: 4px; background: var(--accent-red); }
  .cover-title {
    position: absolute; top: 676px; left: 0; width: 400px; text-align: center;
    font-family: "Source Sans 3", sans-serif; font-weight: 400;
    font-size: 38px; line-height: 48px; color: var(--paper);
  }
</style>
</head>
<body>
<main class="brochure">

  <section class="panel panel--inside">
    <article class="feature feature--top">
      <h2 class="feature__title">Quo dolor voluptatibus id Perferendis</h2>
      <p class="feature__lead">Hic galisum odio aut laborum repellendus ea dolor rerum et molestiae</p>
      <p class="copy">Est corporis fuga quo atque quisquam vel molestiae velit. Et molestiae omnis sit asperiores esse et tempora.</p>
      <p class="copy">Aut dolores placeat aut quidem laboriosam eum illum blanditiis ut aperiam quam aut voluptatem nobis et voluptatem aut libero similique. Vel rerum repudiandae qui sint earum ea ducimus.</p>
    </article>

    <div class="band">
      <div class="band__line" style="top:30px"></div>
      <div class="band__line" style="top:59px"></div>
      <div class="band__line" style="top:86px"></div>
      <div class="band__line" style="top:111px"></div>
    </div>
    <div class="feature-photo" role="img" aria-label="Blue financial newspaper page with percentages, rising chart line and bar graph"></div>

    <article class="feature feature--bottom">
      <h2 class="feature__title">Quo dolor voluptatibus id Perferendis</h2>
      <p class="feature__lead">Hic galisum odio aut laborum repellendus ea dolor rerum et molestiae</p>
      <p class="copy">Est corporis fuga quo atque quisquam vel molestiae velit. Et molestiae omnis sit asperiores esse et tempora.</p>
      <p class="copy">Aut dolores placeat aut quidem laboriosam eum illum blanditiis ut aperiam quam aut voluptatem nobis et voluptatem aut libero similique. Vel rerum repudiandae qui sint earum ea ducimus.</p>
    </article>
  </section>

  <section class="panel panel--back">
    <div class="about">
      <p class="copy">Lorem ipsum dolor sit amet. Quo dolor voluptatibus id perferendis autem ut laboriosam perspiciatis ea dolore dolore ea Quis iure. Id maxime iste eum pariatur galisum et laudantium commodi vel reiciendis cumque. Hic galisum odio aut laborum repellendus ea dolor rerum et molestiae eius est tenetur modi.</p>
      <p class="copy">Est corporis fuga quo atque quisquam vel molestiae velit. Et molestiae omnis sit asperiores esse et tempora.</p>
      <p class="copy">Aut dolores placeat aut quidem laboriosam eum illum blanditiis ut aperiam quam aut voluptatem nobis et voluptatem aut libero similique. Vel rerum repudiandae qui sint earum ea ducimus aspernatur ut dolore rerum! Aut nihil laudantium non sapiente voluptatem et mollitia nihil.</p>
    </div>

    <div class="brand">
      <div class="brand__mark"></div>
      <p class="brand__name">HALVERN ACCOUNTING <span>&amp; CONSULTING, LLC</span></p>
    </div>

    <div class="credential-badge" role="img" aria-label="QDX enrolled agent credential badge"></div>
  </section>

  <section class="panel panel--cover">
    <div class="cover-photo" role="img" aria-label="Hand using a calculator beside a tablet with glowing financial charts"></div>
    <div class="cover-rule"></div>
    <h1 class="cover-title">Tax &amp; Accounting<br>Services</h1>
  </section>

</main>
</body>
</html>
```